Vantor Ridge needs a Business Card Design

We need a business card design for an Information Technology company based in Fairfax Virginia called Vantor Ridge. We want the business card to use our logo colors. We need it to be double-sided. The business card needs to look professional but we would like it to be unique. You can get company information from our web site (http://www.vantorridgellc.example).

Target Market(s)

Target market is Government Agencies and Business Professionals.

Industry/Entity Type

Business

Requirements
Must have
• Must have section for company name, company address, company URL, employee name, title, phone and email. Also must have company logo and space for entering logos.

```html
<!DOCTYPE html>
<html lang="en">
<head>
<meta charset="utf-8">
<title>Vantor Ridge – Business Card</title>
<link rel="stylesheet" href="https://fonts.googleapis.com/css2?family=Lato:wght@400;700&display=swap">
<style>
  :root{
    --stage:#e4e4e6;
    --card:#ffffff;
    --navy:#283a8f;
    --ink:#3a3a3a;
    --muted:#5c5c5c;
    --rule:#8a8a8a;
    --tint:#e2e4f1;
  }
  *{box-sizing:border-box;margin:0;padding:0}
  html,body{width:1200px;height:900px;overflow:hidden}
  body{background:var(--stage);font-family:"Lato",sans-serif;color:var(--ink);position:relative}
  .card{position:absolute;left:267px;width:666px;height:380px;background:var(--card);overflow:hidden;box-shadow:0 6px 18px rgba(0,0,0,.18)}
  .card--contact{top:50px}
  .card--brand{top:470px}

  .wash{position:absolute;top:0;right:0;width:340px;height:100%;
    background:linear-gradient(120deg,rgba(255,255,255,0) 0%,rgba(255,255,255,0) 35%,var(--tint) 100%)}

  .brand{display:flex;align-items:center;gap:14px;position:absolute}
  .brand__mark{width:40px;height:40px;background:var(--navy)}
  .brand__name{font-weight:700;color:var(--navy);font-size:30px;letter-spacing:.5px;text-transform:uppercase;white-space:nowrap}
  .card--contact .brand{left:34px;top:38px}
  .card--brand .brand{left:50%;top:50%;transform:translate(-50%,-50%)}
  .card--brand .brand__mark{width:52px;height:52px}
  .card--brand .brand__name{font-size:40px}

  .person{position:absolute;left:66px;top:148px;width:290px}
  .person__name{font-size:22px;font-weight:400;letter-spacing:1.5px;text-transform:uppercase;color:var(--ink);line-height:1}
  .person__title{font-size:10.5px;font-weight:700;letter-spacing:1px;text-transform:uppercase;color:var(--muted);margin-top:4px}
  .rule{border-top:1.5px dotted var(--rule);margin:5px 0 8px}
  .contacts{list-style:none}
  .contacts li{display:flex;align-items:center;font-size:15px;color:var(--muted);height:22px;white-space:nowrap}
  .contacts svg{width:16px;height:16px;margin-right:22px;flex:none}
  .address{font-size:15.5px;color:var(--muted);line-height:1.45;margin-top:6px}
</style>
</head>
<body>

<section class="card card--contact" aria-label="Business card, contact side">
  <div class="wash" aria-hidden="true"></div>

  <div class="brand">
    <span class="brand__mark"></span>
    <span class="brand__name">Vantor Ridge</span>
  </div>

  <div class="person">
    <h1 class="person__name">Dalen Hurst</h1>
    <p class="person__title">Executive Creative Director</p>
    <div class="rule"></div>
    <ul class="contacts">
      <li>
        <svg viewBox="0 0 16 16"><path d="M4 2l2 3-1.3 1.3a7 7 0 0 0 5 5L11 10l3 2-1 2.5C7 14.5 1.5 9 1.5 3z" fill="none" stroke="var(--muted)" stroke-width="1.2"/></svg>
        : + 65 555-20-0142
      </li>
      <li>
        <svg viewBox="0 0 16 16"><rect x="1.5" y="3.5" width="13" height="9" fill="none" stroke="var(--muted)" stroke-width="1.2"/><path d="M1.5 3.5L8 9l6.5-5.5" fill="none" stroke="var(--muted)" stroke-width="1.2"/></svg>
        : d.hurst@vantorridgellc.example
      </li>
      <li>
        <svg viewBox="0 0 16 16"><circle cx="8" cy="8" r="6.5" fill="none" stroke="var(--muted)" stroke-width="1.2"/><ellipse cx="8" cy="8" rx="3" ry="6.5" fill="none" stroke="var(--muted)" stroke-width="1"/><path d="M1.5 8h13M2.5 5h11M2.5 11h11" stroke="var(--muted)" stroke-width="1"/></svg>
        : www.vantorridgellc.example
      </li>
    </ul>
    <div class="rule"></div>
    <p class="address">4120 Meridian Ave, South<br>Fairfax, Virginia, United States</p>
  </div>
</section>

<section class="card card--brand" aria-label="Business card, brand side">
  <div class="brand">
    <span class="brand__mark"></span>
    <span class="brand__name">Vantor Ridge</span>
  </div>
</section>

</body>
</html>
```